Harwell Systems Advisory - IT Consultancy

I already have a Wordpress site, but not happy with the look and feel or the template I chose.
I want a site as a web presence only, I can configure base SEO myself, but most business is referrals not from a search, so low priority.

My current site is http://harsysadv.example where you can see the sort of content I already have.

Target Market(s)

Business to Business services.

Industry/Entity Type

Consulting

Font styles to use
Sans Serif

Colors
3277b5

Requirements
Must have
• Front Page Template
• Freephone number on front page.
• My Logo and the Venturix logo on the front page
• Page template for Services, Solutions and Portfolio
• Contact Page
• Ability to embed links to Video clips hosted by a third party
Nice to have
• Each page could have a side bar with some common functions, like Request Demo.
• Second Contact Page specifically to Request Demonstrations of Venturix Products, the demo contact page needs to capture some additional information in text boxes and also a check box list of features. The list of features needs to be easily configurable.
• Features to include in checkbox list.
• Contract Management
• Service Desk
• Document Management
• Contract Management
• Business Workflow

```html
<!DOCTYPE html>
<html lang="en">
<head>
<meta charset="utf-8">
<title>Harwell Systems Advisory – IT Consultancy</title>
<link rel="stylesheet" href="https://fonts.googleapis.com/css2?family=Open+Sans:ital,wght@0,400;0,600;0,700;0,800;1,600;1,700&display=swap">
<style>
:root{
  --brand:#0a4c9e;
  --brand-dark:#0b3c7d;
  --brand-bright:#2f8fe8;
  --heading:#3fa0e6;
  --ink:#3b3b3b;
  --muted:#6b6b6b;
  --field:#efefef;
  --frame:#e4e4e4;
  --white:#ffffff;
  --black:#111111;
}
*{box-sizing:border-box;margin:0;padding:0}
html,body{width:1200px;height:2880px;overflow:hidden}
body{background:var(--frame);font-family:"Open Sans",Arial,sans-serif;color:var(--ink);position:relative}
.page{position:absolute;left:15px;top:0;width:1170px;height:2880px;background:var(--white)}
.abs{position:absolute}
.section-title{position:absolute;left:0;width:100%;text-align:center;font-style:italic;font-weight:700;font-size:23px;color:var(--heading)}
.section-title.dark{color:var(--brand)}
.btn-outline{position:absolute;border:2px solid #fff;color:#fff;font-size:12px;font-weight:600;text-transform:uppercase;display:flex;align-items:center;justify-content:center;border-radius:3px}
.chevron{position:absolute;left:0;width:1170px;height:32px}

/* header */
.brand-name{left:25px;top:36px;font-size:30px;font-weight:700;color:var(--brand);letter-spacing:1px;line-height:1.1}
.brand-name small{display:block;font-size:15px;letter-spacing:2px;font-weight:700;text-transform:uppercase}
.call-label{left:793px;top:44px;font-size:14px;font-weight:700;color:#333}
.call-number{left:791px;top:60px;font-size:33px;font-weight:600;color:var(--brand)}

/* nav */
.main-nav{left:0;top:129px;width:1170px;height:50px;background:var(--brand-dark)}
.main-nav span{position:absolute;top:16px;transform:translateX(-50%);color:#fff;font-size:13px;font-weight:700;white-space:nowrap}
.main-nav span.active{color:var(--heading)}

/* hero */
.hero{left:0;top:179px;width:1170px;height:551px;background:radial-gradient(ellipse at 35% 40%,#3a5c80 0%,#1b2a3d 40%,#080c14 100%)}
.demo-panel{left:705px;top:294px;width:398px;height:351px;border:2px solid #9fb0c4;border-radius:4px;background:rgba(8,14,26,.55)}
.demo-head{left:695px;top:294px;width:423px;height:52px;background:var(--brand);color:#fff;font-weight:700;font-size:27px;display:flex;align-items:center;justify-content:center}
.demo-field{position:absolute;background:rgba(3,8,18,.85);color:#fff;font-size:12px;font-weight:600;padding:6px 10px}
.demo-submit{left:820px;top:597px;width:201px;height:29px;background:linear-gradient(#1c5fb5,#0a3f86);color:#fff;font-size:13px;font-weight:700;display:flex;align-items:center;justify-content:center}

/* services */
.services{left:0;top:730px;width:1170px;height:422px;background:var(--brand)}
.service{position:absolute;top:80px;width:170px;height:185px;text-align:center;color:#fff;font-style:italic;font-weight:700;font-size:19px;line-height:1.15}
.service.active{background:var(--brand-bright);border-radius:4px}
.service.active::after{content:"";position:absolute;left:70px;bottom:-14px;border:15px solid transparent;border-bottom:0;border-top-color:var(--brand-bright)}
.service svg{display:block;margin:22px auto 10px}
.service .wordmark{display:block;height:106px;padding-top:50px;font-style:normal;font-size:24px;font-weight:700}
.services-copy{left:127px;top:300px;width:920px;color:#fff;font-size:14px;line-height:1.5}

/* solutions */
.solutions-mark{left:96px;top:1290px;width:240px;height:76px;display:flex;align-items:center;justify-content:center;font-size:50px;font-weight:800;color:var(--brand)}
.solutions-copy{left:359px;top:1276px;width:790px;font-size:14px;line-height:1.55;color:#444}
.btn-solid{left:525px;top:1405px;width:122px;height:30px;background:var(--brand);color:#fff;font-size:12px;font-weight:700;display:flex;align-items:center;justify-content:center;border-radius:3px}

/* portfolio */
.portfolio{left:0;top:1430px;width:1170px;height:510px;background:var(--brand)}
.card{position:absolute;top:144px;width:271px;height:331px;background:#fff;border-radius:4px;overflow:hidden}
.card-logo{height:184px;display:flex;align-items:center;justify-content:center;gap:10px;font-size:28px;font-weight:700;color:var(--brand);text-align:center;line-height:1.1}
.card-body{height:147px;background:linear-gradient(#ffffff,#dcdcdc);padding:12px 16px}
.card-body h3{font-size:14px;font-weight:700;color:#333;text-transform:uppercase}
.card-body p{font-size:13px;line-height:1.3;color:#555;margin-top:3px}
.card-btn{position:absolute;left:74px;bottom:20px;width:122px;height:30px;border:2px solid var(--brand);color:var(--brand);font-size:12px;font-weight:700;display:flex;align-items:center;justify-content:center;border-radius:3px;background:#fff}
.dot{width:34px;height:34px;border-radius:50%;background:var(--brand);flex:none}

/* clients */
.clients-sub{left:0;top:2054px;width:1170px;text-align:center;font-size:14px;color:#555}
.client{position:absolute;top:2126px;height:46px;display:flex;align-items:center;font-size:26px;font-weight:700;color:var(--brand);white-space:nowrap}

/* blog */
.blog{left:0;top:2198px;width:1170px;height:356px;background:var(--brand)}
.blog-img{position:absolute;top:133px;width:135px;height:132px}
.blog-date{position:absolute;top:136px;color:#fff;font-size:15px;font-weight:700}
.blog-text{position:absolute;top:168px;width:300px;color:#fff;font-size:14px;font-weight:700;line-height:1.4}
.read-more{position:absolute;top:294px;width:150px;height:28px;background:var(--black);color:#fff;font-size:12px;font-weight:700;display:flex;align-items:center;padding-left:14px;border-radius:4px}
.read-more svg{position:absolute;right:12px;top:9px}

/* contact */
.contact-line{position:absolute;left:129px;font-size:15px;color:#444;line-height:1.4}
.contact-icon{position:absolute;left:100px}
.field{position:absolute;background:var(--field);font-size:13px;color:#555;padding:8px 14px}
.send{left:771px;top:2736px;width:104px;height:38px;background:var(--black);color:#fff;font-size:14px;font-weight:700;display:flex;align-items:center;justify-content:center}
.social{left:148px;top:2790px;display:flex;gap:8px}
.social span{width:17px;height:17px;border-radius:50%;background:#555}
.footer{left:0;top:2834px;width:1170px;height:27px;background:var(--brand);color:#fff;font-size:10px;font-weight:700;display:flex;align-items:center;justify-content:center}
</style>
</head>
<body>
<div class="page">

  <!-- Header -->
  <div class="abs brand-name">HARWELL<small>Systems Advisory</small></div>
  <svg class="abs" style="left:749px;top:50px" width="44" height="44" viewBox="0 0 44 44" aria-hidden="true">
    <circle cx="22" cy="22" r="20" fill="none" stroke="#0a4c9e" stroke-width="3"/>
    <path d="M15 12c2-1 3 0 4 3l1 3c0 1-1 2-2 3 1 3 3 5 6 6 1-1 2-2 3-2l3 1c3 1 4 2 3 4-1 3-4 4-7 3-6-2-11-7-13-13-1-3 0-6 2-8z" fill="#0a4c9e"/>
  </svg>
  <div class="abs call-label">CALL FOR A FREE CONSULTATION</div>
  <div class="abs call-number">+44 (0) 80 00 55 21 90</div>

  <!-- Navigation -->
  <nav class="abs main-nav">
    <span class="active" style="left:142px">HOME</span>
    <span style="left:267px">SERVICES</span>
    <span style="left:411px">VENTURIX SOLUTIONS</span>
    <span style="left:621px">PORTFOLIO</span>
    <span style="left:772px">CLIENTS</span>
    <span style="left:874px">BLOG</span>
    <span style="left:1007px">CONTACT US</span>
  </nav>

  <!-- Hero -->
  <div class="abs hero" role="img" aria-label="Photo of a hand touching a glowing digital interface with technology icons"></div>
  <div class="abs demo-panel"></div>
  <div class="abs demo-head">REQUEST A DEMO</div>
  <div class="demo-field" style="left:720px;top:367px;width:181px;height:27px">Name</div>
  <div class="demo-field" style="left:910px;top:367px;width:181px;height:27px">Email Address</div>
  <div class="demo-field" style="left:720px;top:405px;width:181px;height:29px">Phone Number</div>
  <div class="demo-field" style="left:910px;top:405px;width:181px;height:29px">Features
    <svg style="position:absolute;right:10px;top:11px" width="12" height="7" viewBox="0 0 12 7"><path d="M0 0h12L6 7z" fill="#fff"/></svg>
  </div>
  <div class="demo-field" style="left:720px;top:445px;width:371px;height:131px">Message</div>
  <div class="abs demo-submit">SUBMIT</div>

  <!-- Services -->
  <section class="abs services">
    <h2 class="section-title" style="top:34px">Services</h2>
    <div class="service active" style="left:125px">
      <svg width="86" height="86" viewBox="0 0 86 86" aria-hidden="true">
        <circle cx="43" cy="43" r="30" fill="none" stroke="#fff" stroke-width="3"/>
        <circle cx="43" cy="43" r="12" fill="#fff"/>
        <circle cx="43" cy="11" r="9" fill="var(--brand-bright)" stroke="#fff" stroke-width="3"/>
        <circle cx="43" cy="75" r="9" fill="var(--brand-bright)" stroke="#fff" stroke-width="3"/>
        <circle cx="11" cy="43" r="9" fill="var(--brand-bright)" stroke="#fff" stroke-width="3"/>
        <circle cx="75" cy="43" r="9" fill="var(--brand-bright)" stroke="#fff" stroke-width="3"/>
      </svg>
      Project<br>Management
    </div>
    <div class="service" style="left:320px">
      <svg width="100" height="100" viewBox="0 0 100 100" aria-hidden="true">
        <circle cx="50" cy="52" r="44" fill="none" stroke="#fff" stroke-width="7"/>
        <circle cx="50" cy="52" r="28" fill="none" stroke="#fff" stroke-width="6"/>
        <circle cx="50" cy="52" r="10" fill="#fff"/>
        <path d="M50 52L88 12" stroke="#fff" stroke-width="4"/>
        <path d="M82 8l10-4-4 10z" fill="#fff"/>
      </svg>
      Solutions<br>Design
    </div>
    <div class="service" style="left:514px"><span class="wordmark">Venturix</span>Venturix</div>
    <div class="service" style="left:708px">
      <svg width="100" height="90" viewBox="0 0 100 90" aria-hidden="true">
        <path d="M50 8c24 0 44 13 44 30S74 68 50 68c-5 0-9 0-13-2L16 80l6-18C12 56 6 48 6 38 6 21 26 8 50 8z" fill="#fff"/>
        <circle cx="32" cy="38" r="6" fill="var(--brand)"/>
        <circle cx="50" cy="38" r="6" fill="var(--brand)"/>
        <circle cx="68" cy="38" r="6" fill="var(--brand)"/>
      </svg>
      Consulting
    </div>
    <div class="service" style="left:904px">
      <svg width="96" height="92" viewBox="0 0 96 92" aria-hidden="true">
        <path d="M48 26V14c0-6 4-8 10-8h14" stroke="#fff" stroke-width="4" fill="none"/>
        <rect x="4" y="26" width="88" height="60" rx="6" fill="none" stroke="#fff" stroke-width="5"/>
        <g fill="#fff">
          <rect x="16" y="38" width="10" height="8"/><rect x="31" y="38" width="10" height="8"/><rect x="46" y="38" width="10" height="8"/><rect x="61" y="38" width="10" height="8"/><rect x="76" y="38" width="6" height="8"/>
          <rect x="16" y="51" width="10" height="8"/><rect x="31" y="51" width="10" height="8"/><rect x="46" y="51" width="10" height="8"/><rect x="61" y="51" width="10" height="8"/><rect x="76" y="51" width="6" height="8"/>
          <rect x="24" y="64" width="48" height="8"/>
        </g>
      </svg>
      Technologies
    </div>
    <p class="abs services-copy">Lorem ipsum dolor sit amet, consectetuer adipiscing elit, sed diam nonummy nibh euismod tincidunt ut laoreet dolore magna aliquam erat volutpat. Ut wisi enim ad minim veniam, quis nostrud exerci tation ullamcorper suscipit lobortis nisl ut aliquip ex ea commodo consequat. Duis autem veleum iriure dolor in hendrerit in vulputate velit esse molestie consequat, vel illum dolore eu feugiat nulla facilisis at vero.</p>
    <div class="btn-outline" style="left:525px;top:389px;width:122px;height:31px">Discover More</div>
  </section>
  <svg class="chevron" style="top:1151px" viewBox="0 0 1170 32" preserveAspectRatio="none" aria-hidden="true"><path d="M0 0H1170L585 24z" fill="#0a4c9e"/></svg>

  <!-- Venturix Solutions -->
  <h2 class="section-title dark" style="top:1230px">Venturix Solutions</h2>
  <div class="abs solutions-mark">Venturix</div>
  <p class="abs solutions-copy">Lorem ipsum dolor sit amet, consectetuer adipiscing elit, sed diam nonummy nibh euismod tincidunt ut laoreet dolore magna aliquam erat volutpat. Ut wisi enim ad minim veniam, quis nostrud exerci tation ullamcorper suscipit lobortis nisl ut aliquip ex ea commodo consequat. Duis autem veleum iriure dolor in hendrerit in vulputate velit esse molestie consequat, vel illum dolore eu feugiat nulla facilisis at vero eros et accumsan et iustoodio dignissim qui blandit praesent luptatum zzril delenit augue duis dolore te feugait nulla facilisi. Nam liber tempor cum soluta.</p>
  <div class="abs btn-solid">DISCOVER MORE</div>

  <!-- Portfolio -->
  <section class="abs portfolio">
    <svg class="chevron" style="top:-1px" viewBox="0 0 1170 32" preserveAspectRatio="none" aria-hidden="true"><path d="M0 0H1170L585 26z" fill="#fff"/></svg>
    <h2 class="section-title" style="top:86px">Portfolio</h2>
    <article class="card" style="left:30px">
      <div class="card-logo"><span class="dot"></span>Meridane<br>Pharma</div>
      <div class="card-body"><h3>Meridane Pharma</h3><p>Lorem ipsum dolor sit amet, consectetuer adipiscing elit, sed diam nonummy nibh euismod tincidunt.</p></div>
      <div class="card-btn">DISCOVER MORE</div>
    </article>
    <article class="card" style="left:310px">
      <div class="card-logo">BREWLINE<br>EXPRESS</div>
      <div class="card-body"><h3>Brewline Express</h3><p>Lorem ipsum dolor sit amet, consectetuer adipiscing elit, sed diam nonummy nibh euismod tincidunt.</p></div>
      <div class="card-btn">DISCOVER MORE</div>
    </article>
    <article class="card" style="left:590px">
      <div class="card-logo">PLAY FAIR<br>SPORTS</div>
      <div class="card-body"><h3>Play Fair Sports</h3><p>Lorem ipsum dolor sit amet, consectetuer adipiscing elit, sed diam nonummy nibh euismod tincidunt.</p></div>
      <div class="card-btn">DISCOVER MORE</div>
    </article>
    <article class="card" style="left:870px">
      <div class="card-logo"><span class="dot"></span>Shopcast</div>
      <div class="card-body"><h3>Shopcast</h3><p>Lorem ipsum dolor sit amet, consectetuer adipiscing elit, sed diam nonummy nibh euismod tincidunt.</p></div>
      <div class="card-btn">DISCOVER MORE</div>
    </article>
  </section>
  <svg class="chevron" style="top:1939px" viewBox="0 0 1170 40" preserveAspectRatio="none" aria-hidden="true"><path d="M0 0H1170L585 38z" fill="#0a4c9e"/></svg>

  <!-- Clients -->
  <h2 class="section-title dark" style="top:2009px">Clients</h2>
  <p class="abs clients-sub">We have worked on projects for many prestigious clients since 2010, including:</p>
  <svg class="abs" style="left:72px;top:2134px" width="16" height="30" viewBox="0 0 16 30" aria-hidden="true"><path d="M14 2L2 15l12 13" stroke="#888" stroke-width="2.5" fill="none"/></svg>
  <svg class="abs" style="left:1083px;top:2134px" width="16" height="30" viewBox="0 0 16 30" aria-hidden="true"><path d="M2 2l12 13L2 28" stroke="#888" stroke-width="2.5" fill="none"/></svg>
  <div class="client" style="left:135px;font-size:22px">Meridane Pharma</div>
  <div class="client" style="left:375px;font-size:22px">Shopcast</div>
  <div class="client" style="left:512px">Venturix</div>
  <div class="client" style="left:745px;font-size:22px;gap:10px"><span class="dot" style="width:30px;height:30px"></span>Fenwick University</div>

  <!-- Blog -->
  <section class="abs blog">
    <svg class="chevron" style="top:-1px;height:46px" viewBox="0 0 1170 46" preserveAspectRatio="none" aria-hidden="true"><path d="M0 0H1170L585 44z" fill="#fff"/></svg>
    <h2 class="section-title" style="top:83px">Blog</h2>
    <div class="blog-img" style="left:71px;background:linear-gradient(135deg,#f3f4f6,#b9c2cc)" role="img" aria-label="Photo of office paperwork and a laptop on a desk"></div>
    <div class="blog-date" style="left:231px">December 18, 2015</div>
    <p class="blog-text" style="left:231px">Lorem ipsum dolor sit amet, consectetuer adipiscing elit, sed diam nonummy nibh euismod tincidunt ut laoreet dolore magna aliquam erat volutpat. Ut wisi enim ad minim veniam, quis nostrud exerci tation ullamcorper.</p>
    <div class="read-more" style="left:231px">READ MORE<svg width="7" height="11" viewBox="0 0 7 11"><path d="M1 1l4.5 4.5L1 10" stroke="#fff" stroke-width="2" fill="none"/></svg></div>
    <div class="blog-img" style="left:613px;background:radial-gradient(circle at 40% 45%,#6fb6ff,#1a4fa3 55%,#071a3d)" role="img" aria-label="Illustration of a glowing blue globe network"></div>
    <div class="blog-date" style="left:770px">December 22, 2015</div>
    <p class="blog-text" style="left:770px">Lorem ipsum dolor sit amet, consectetuer adipiscing elit, sed diam nonummy nibh euismod tincidunt ut laoreet dolore magna aliquam erat volutpat. Ut wisi enim ad minim veniam, quis nostrud exerci tation ullamcorper.</p>
    <div class="read-more" style="left:770px">READ MORE<svg width="7" height="11" viewBox="0 0 7 11"><path d="M1 1l4.5 4.5L1 10" stroke="#fff" stroke-width="2" fill="none"/></svg></div>
  </section>
  <svg class="chevron" style="top:2553px" viewBox="0 0 1170 20" preserveAspectRatio="none" aria-hidden="true"><path d="M0 0H1170L585 18z" fill="#0a4c9e"/></svg>

  <!-- Contact -->
  <h2 class="section-title dark" style="top:2599px">Contact</h2>
  <svg class="contact-icon" style="top:2642px" width="14" height="20" viewBox="0 0 14 20" aria-hidden="true"><path d="M7 0a7 7 0 0 1 7 7c0 5-7 13-7 13S0 12 0 7a7 7 0 0 1 7-7z" fill="#666"/><circle cx="7" cy="7" r="2.5" fill="#fff"/></svg>
  <p class="contact-line" style="top:2640px">Lorem ipsum drive, Suite # 108<br>Manchester</p>
  <svg class="contact-icon" style="top:2708px" width="18" height="14" viewBox="0 0 18 14" aria-hidden="true"><path d="M1 4c0-3 16-3 16 0v2h-4V4H5v2H1z" fill="#666"/><rect x="3" y="7" width="12" height="7" rx="1" fill="#666"/></svg>
  <p class="contact-line" style="top:2705px">+44 (0) 80 00 55 21 90</p>
  <svg class="contact-icon" style="top:2752px" width="18" height="13" viewBox="0 0 18 13" aria-hidden="true"><rect width="18" height="13" rx="1" fill="#666"/><path d="M1 1l8 6 8-6" stroke="#fff" stroke-width="1.5" fill="none"/></svg>
  <p class="contact-line" style="top:2747px">info@harsysadv.example</p>
  <div class="abs social" aria-label="Social links"><span></span><span></span><span></span><span></span><span></span></div>

  <div class="field" style="left:461px;top:2640px;width:298px;height:38px">Name</div>
  <div class="field" style="left:461px;top:2688px;width:298px;height:38px">Email</div>
  <div class="field" style="left:461px;top:2736px;width:298px;height:38px">Phone</div>
  <div class="field" style="left:771px;top:2640px;width:300px;height:86px">Message</div>
  <div class="abs send">SEND</div>

  <footer class="abs footer">COPYRIGHT © 2016 HARWELL SYSTEMS ADVISORY LTD.</footer>
</div>
</body>
</html>
```